BRAMWICK FORDE FISH BAR

We need a flyer design for our fish and chip shop, we are looking for something bright and eye catching with some images possibly in the theme of the ocean but interested in other ideas.
we need the flyer to include the following information;
address- 27-29 the mill lane
ashcombe vale
0k41 7tz
phone number 01632 960482
opening hours - Thursday,friday,saturday lunchtimes 12-2pm

Tuesday,wednesday,thursday evenings 4.30-9pm

Friday, Saturday evenings 4.30-9.30pm

card payments excepted.

traditional fish and chips
Aberdeen angus chargrilled steak burgers (free range, organic meat)
kebabs (donner and chicken)

Pension day every Thursday, 50p off any meal deal

special offer,
£1 off large fish and chips with this leaflet

Shop

• we would like some images, possibly with an ocean theme but other interested in other ideas to do with fish and chips.

```html
<!DOCTYPE html>
<html lang="en">
<head>
<meta charset="utf-8">
<title>Bramwick Forde Fish Bar – Flyer</title>
<link rel="stylesheet" href="https://fonts.googleapis.com/css2?family=Anton&family=Michroma&family=Righteous&family=Delius&display=swap">
<style>
  :root {
    --backdrop: #e9e7ea;
    --paper: #ffffff;
    --title-blue: #8fd0f2;
    --title-shadow: #4f7f9c;
    --offer-blue: #3f8fd0;
    --orange: #e8901c;
    --sea-deep: #1a9be0;
    --sea-light: #cdebfb;
    --ink: #1c1c1c;
    --fry-light: #f6d79a;
    --fry-deep: #d89a4a;
  }
  * { box-sizing: border-box; margin: 0; padding: 0; }
  html, body {
    width: 1200px; height: 1134px; overflow: hidden;
    background: var(--backdrop);
  }
  .flyer {
    position: absolute; left: 170px; top: 47px;
    width: 860px; height: 1040px;
    background: var(--paper);
    overflow: hidden;
    box-shadow: 0 6px 24px rgba(0,0,0,.15);
  }
  .food-photo {
    position: absolute; left: 20px; top: 120px; width: 820px; height: 320px;
    border-radius: 40% 30% 35% 40% / 40%;
    background: radial-gradient(ellipse at 55% 45%, var(--fry-light) 0%, var(--fry-deep) 55%, rgba(255,255,255,0) 78%);
  }
  .shop-title {
    position: absolute; left: 0; right: 0; top: 26px;
    text-align: center; white-space: nowrap;
    font-family: "Anton", sans-serif; font-size: 96px; line-height: 1;
    color: var(--title-blue);
    text-shadow: 4px 4px 0 var(--title-shadow);
  }
  .offer-heading {
    position: absolute; left: 70px; top: 440px;
    font-family: "Michroma", sans-serif; font-size: 50px; line-height: 1.1; letter-spacing: 4px;
    color: var(--offer-blue);
    text-shadow: 2px 2px 0 #fff;
  }
  .offer-main {
    position: absolute; left: 36px; right: 20px; top: 516px;
    font-family: "Righteous", sans-serif; font-size: 28px; line-height: 1.2; text-transform: uppercase;
    color: var(--orange); white-space: nowrap;
  }
  .offer-sub {
    position: absolute; left: 80px; top: 562px;
    font-family: "Michroma", sans-serif; font-size: 17px; letter-spacing: 3px;
    color: var(--offer-blue); text-transform: uppercase; white-space: nowrap;
  }
  .menu {
    position: absolute; left: 36px; top: 600px; list-style: none;
    font-family: "Delius", cursive; font-size: 40px; line-height: 58px;
    color: var(--orange); white-space: nowrap;
  }
  .sea-art {
    position: absolute; left: 0; right: 0; bottom: 0; height: 250px;
    background: linear-gradient(175deg, rgba(255,255,255,0) 0%, var(--sea-light) 30%, var(--sea-deep) 100%);
  }
  .shop-details {
    position: absolute; left: 36px; top: 862px;
    font-family: Arial, Helvetica, sans-serif; font-size: 19px; line-height: 22px;
    color: var(--ink);
  }
  .shop-details .contact { margin-top: 14px; font-size: 21px; line-height: 24px; }
  .card-note {
    position: absolute; right: 40px; top: 890px;
    font-family: Arial, Helvetica, sans-serif; font-size: 18px; color: var(--ink);
  }
</style>
</head>
<body>
  <main class="flyer">
    <div class="food-photo" role="img" aria-label="Photo of golden battered fish with parsley on a bed of chips"></div>
    <h1 class="shop-title">FISH AND CHIP SHOP</h1>

    <h2 class="offer-heading">SPECIAL OFFER</h2>
    <p class="offer-main">£1 off large fish and chips with this leaflet</p>
    <p class="offer-sub">Every Thursday, 50p off any meal deal</p>

    <ul class="menu">
      <li>traditional fish and chips</li>
      <li>Aberdeen angus chargrilled steak burgers</li>
      <li>(free range, organic meat)</li>
      <li>kebabs (donner and chicken)</li>
    </ul>

    <div class="sea-art" role="img" aria-label="Illustration of breaking blue ocean waves"></div>

    <section class="shop-details">
      <p>opening hours</p>
      <p>Thursday,friday,saturday lunchtimes 12-2pm</p>
      <p>Tuesday,wednesday,thursday evenings 4.30-9pm</p>
      <p>Friday, Saturday evenings 4.30-9.30pm</p>
      <p class="contact">address: 27-29 the mill lane,ashcombe vale,0k41 7tz<br>phone number 01632 960482</p>
    </section>
    <p class="card-note">*card payments excepted</p>
  </main>
</body>
</html>
```